Business card design for IT consulting company

Looking for a simple, modern, clean business card design.
Open to reworking our existing logo.

Attached is our current business cards which we do not like.
Ideally double sided with something simple on the back.
Rectangle / Horizonal only.
No rounded edges on the card.
White as the dominate color is preferred.

Target Market(s)

clients, legal, oil & gas, medical, professionals

Industry/Entity Type

IT, tech, consulting

Contact Information for Business Card

Name, Title, email, phone, cell, website

Font styles to use
Sans Serif

Requirements
Must have
• Clean design
Should not have
• loud colors or unusual fonts, etc

```html
<!DOCTYPE html>
<html lang="en">
<head>
<meta charset="utf-8">
<title>Nexlo Business Card</title>
<link rel="stylesheet" href="https://fonts.googleapis.com/css2?family=Inter:ital,wght@0,400;0,500;0,700;0,800;1,400&display=swap">
<style>
  :root {
    --page-bg: #d9d8d6;
    --card-bg: #222222;
    --text-light: #f2f2f2;
    --text-muted: #e4e4e4;
    --accent-yellow: #f5c842;
    --font-main: "Inter", Arial, sans-serif;
  }
  * { box-sizing: border-box; margin: 0; padding: 0; }
  html, body {
    width: 1200px;
    height: 1000px;
    overflow: hidden;
    background: var(--page-bg);
    font-family: var(--font-main);
  }
  .sheet {
    width: 1200px;
    height: 1000px;
    display: flex;
    flex-direction: column;
    align-items: center;
    justify-content: center;
    gap: 56px;
  }
  .card {
    width: 700px;
    height: 400px;
    background: var(--card-bg);
    display: flex;
    align-items: center;
    padding: 0 70px;
    box-shadow: 0 10px 30px rgba(0,0,0,0.18);
  }
  .brand {
    display: flex;
    align-items: center;
    gap: 16px;
    width: 300px;
    flex-shrink: 0;
  }
  .brand-square {
    width: 46px;
    height: 46px;
    background: var(--accent-yellow);
  }
  .brand-name {
    font-weight: 700;
    font-size: 46px;
    color: var(--text-light);
    letter-spacing: -0.5px;
  }
  .tagline {
    color: var(--text-light);
    font-size: 24px;
    font-weight: 400;
    line-height: 1.2;
  }
  .contact { color: var(--text-light); }
  .contact-name {
    color: var(--accent-yellow);
    font-weight: 800;
    font-size: 28px;
    line-height: 1.1;
  }
  .contact-title {
    font-style: italic;
    font-size: 20px;
    color: var(--text-muted);
    margin-bottom: 22px;
  }
  .contact-list {
    display: grid;
    grid-template-columns: 48px auto;
    row-gap: 3px;
    align-items: baseline;
  }
  .contact-label {
    font-size: 12px;
    font-weight: 700;
  }
  .contact-value {
    font-size: 19px;
    font-weight: 400;
  }
</style>
</head>
<body>
  <main class="sheet">
    <section class="card card-front">
      <div class="brand">
        <span class="brand-square"></span>
        <span class="brand-name">Nexlo</span>
      </div>
      <p class="tagline">Expertly Managed<br>IT Services and<br>Tech Support Solutions</p>
    </section>

    <section class="card card-back">
      <div class="brand">
        <span class="brand-square"></span>
        <span class="brand-name">Nexlo</span>
      </div>
      <div class="contact">
        <h1 class="contact-name">Daniel Reyes</h1>
        <p class="contact-title">IT Consultant</p>
        <dl class="contact-list">
          <dt class="contact-label">Ph</dt><dd class="contact-value">(888) 555-0142</dd>
          <dt class="contact-label">Mob</dt><dd class="contact-value">(604) 555-0187</dd>
          <dt class="contact-label">@</dt><dd class="contact-value">daniel.reyes@nexlo.ca</dd>
          <dt class="contact-label">Web</dt><dd class="contact-value">www.nexlo.ca</dd>
        </dl>
      </div>
    </section>
  </main>
</body>
</html>
```